Infographic on 10 Step Learning Course Framework

I have a 10 step guide I need to be put into a clean, modern, design template.. very much like an infographic (although more text obviously). Need a really quick turnaround time and will pay $120 extra to the winner!

We are a modern online learning company, and like clean and sophisticated design (inspirated is Scandanavian design, Helvetic a, Raleway type fonts with warm earthy colors and tones). Visit www.mindharborlabs.com for more inspiration. Also, download our 'Shape Lessons Toward Revenue' eBook on our Resources section to get more of a sense.

Target Market(s)

Online Learning instructional designers

Industry/Entity Type

Business Software

Font styles to use
Sans Serif

Requirements
Must have
• The entire copy listed
Nice to have
• N/A
Should not have
• Stock imagery or cheesy graphics / artclip

```html
<!DOCTYPE html>
<html lang="en">
<head>
<meta charset="utf-8">
<title>Mind Harbor Labs — 10 Step Proprietary Learning Framework</title>
<link rel="stylesheet" href="https://fonts.googleapis.com/css2?family=Raleway:ital,wght@0,400;0,500;0,600;0,700;0,800;0,900;1,400&display=swap">
<style>
:root{
  --espresso:#2a1a14;
  --umber:#4a2b22;
  --olive:#6a6a34;
  --rust:#8a5420;
  --cream:#f4e4c4;
  --sand:#dcaa76;
  --taupe:#c8ad8a;
  --taupe-light:#d8c3a2;
  --ink:#3b2a20;
  --white:#ffffff;
  --line:#4a2b22;
}
*{box-sizing:border-box;margin:0;padding:0}
html,body{width:1200px;height:4800px;overflow:hidden}
body{font-family:"Raleway",Helvetica,Arial,sans-serif;color:var(--ink);background:var(--cream);position:relative;display:flex;flex-direction:column}

/* brand name */
.brand{display:inline-flex;align-items:center;gap:10px;font-weight:600;font-size:20px;color:var(--white)}
.brand-square{width:12px;height:12px;background:var(--white)}

/* hero */
.hero{position:relative;height:815px;flex:none;color:var(--white);text-align:center}
.hero-photo{position:absolute;inset:0;background:linear-gradient(160deg,#5a3a2c 0%,#3a241b 45%,#22150f 100%)}
.hero-content{position:relative;padding-top:34px}
.hero-title{font-weight:900;font-size:180px;line-height:1;letter-spacing:-2px;margin-top:60px}
.hero-sub{display:flex;align-items:center;justify-content:center;gap:26px;font-weight:800;font-size:54px;line-height:1;margin-top:24px;text-transform:uppercase}
.hero-sub::before,.hero-sub::after{content:"";width:150px;height:4px;background:var(--white)}
.hero-sub2{font-weight:800;font-size:54px;text-transform:uppercase;margin-top:10px}
.hero-intro{width:640px;margin:110px auto 0;text-align:left;font-size:18px;line-height:1.5}
.hero-intro p+p{margin-top:18px}

/* note */
.note{height:185px;flex:none;background:var(--olive);color:var(--white);display:flex;align-items:center;padding:0 80px 0 115px;gap:110px}
.note-label{font-weight:800;font-size:46px;letter-spacing:1px}
.note-text{font-size:18px;line-height:1.45;max-width:680px}

/* process intro */
.process{flex:none;padding-bottom:60px}
.process-heading{text-align:center;padding-top:70px}
.process-heading h2{font-weight:900;font-size:52px;text-transform:uppercase;color:var(--espresso)}
.process-heading p{font-size:24px;font-weight:500;margin-top:4px}

/* step rows */
.step{display:grid;grid-template-columns:110px 330px 92px 608px 60px;align-items:start}
.step-label{grid-column:2;text-align:right;font-weight:900;font-size:30px;line-height:1.12;text-transform:uppercase;color:var(--espresso)}
.step-label small{display:block;font-size:16px;font-weight:700;text-transform:none;line-height:1.35;margin-top:10px}
.step-num{grid-column:3;justify-self:center;width:70px;height:70px;border-radius:50%;background:var(--umber);color:var(--white);font-weight:600;font-size:28px;display:flex;align-items:center;justify-content:center;position:relative;z-index:2}
.step-body{grid-column:4;padding-left:8px;font-size:17px;line-height:1.45}
.step-body p+p{margin-top:16px}

/* stage band */
.stage{height:190px;flex:none;background:var(--sand);display:grid;grid-template-columns:110px 330px 92px 560px;align-items:center}
.stage-label{grid-column:2;text-align:right;font-weight:800;font-size:20px;text-transform:uppercase;color:var(--espresso)}
.stage-dot{grid-column:3;justify-self:center;width:26px;height:26px;border-radius:50%;background:var(--umber);position:relative;z-index:2}
.stage-text{grid-column:4;padding-left:8px;font-size:17px;line-height:1.45}

/* options */
.options{flex:none;padding:55px 0 70px}
.options-head{margin-left:560px;width:540px;font-size:19px;line-height:1.3}
.options-head strong{display:block;font-weight:900;text-transform:uppercase;font-size:20px}
.pair{grid-column:4;display:grid;grid-template-columns:240px 255px;column-gap:22px;margin-left:20px}
.cell{padding:20px 18px;font-size:15px;line-height:1.42}
.cell-self{background:var(--taupe)}
.cell-guided{background:var(--taupe-light)}
.cell .aside{display:block;font-style:italic;font-size:12px;margin-top:12px;opacity:.75}
.path-head{margin-top:26px}
.path-head .cell{text-align:center;color:var(--white);font-size:17px;line-height:1.25;padding:34px 14px 58px}
.path-head .cell-self{background:var(--olive)}
.path-head .cell-guided{background:var(--rust)}
.path-head b{display:block;font-weight:900;font-size:20px;text-transform:uppercase}
.options .step{margin-top:10px}
.options .step-label,.options .step-num{margin-top:30px}
.options .step.plain{margin-top:34px}
.options .step.plain .step-label,.options .step.plain .step-num{margin-top:0}
.closing{text-align:center;font-weight:900;font-size:28px;line-height:1.3;color:var(--espresso);margin-top:60px}

/* outro */
.outro{flex:1;background:var(--rust);color:var(--white);display:flex;align-items:flex-end;justify-content:center;padding-bottom:60px}
.outro p{width:880px;font-size:18px;line-height:1.5}

/* footer */
.footer{height:150px;flex:none;background:var(--espresso);color:var(--white);text-align:center;padding-top:40px}
.footer-url{font-size:16px;margin-top:14px}

/* timeline */
.timeline{position:absolute;left:535px;top:1250px;width:3px;height:2900px;background:var(--line);z-index:1}
</style>
</head>
<body>

<header class="hero">
  <div class="hero-photo" role="img" aria-label="Warm, dimly lit photo of a team working together in an office"></div>
  <div class="hero-content">
    <div class="brand"><span class="brand-square"></span>Mind Harbor Labs</div>
    <h1 class="hero-title">10 STEP</h1>
    <div class="hero-sub">Proprietary</div>
    <div class="hero-sub2">Learning Framework</div>
    <div class="hero-intro">
      <p>How we utilize our time-tested methods to take your Big Ideas and turn them into a compelling and profitable learning experience.</p>
      <p>Based on our work with hundreds of clients, we have developed the following process which can be used by new clients or existing clients who seek to upgrade their current offerings in the platform.</p>
    </div>
  </div>
</header>

<section class="note">
  <div class="note-label">NOTE</div>
  <p class="note-text">This process is not always followed sequentially from Steps 1-10, as clients come to us at different levels of preparedness. We will work with you to identify where you are in your journey and will advise you accordingly.</p>
</section>

<section class="process">
  <div class="process-heading">
    <h2>Here's the Process</h2>
    <p>of our proprietary 10 Step Learning Framework:</p>
  </div>

  <div class="step" style="margin-top:55px">
    <h3 class="step-label">Complete Your Learning Experience Questionnaire</h3>
    <div class="step-num">01</div>
    <div class="step-body"><p>The first step in the process is for you to complete our Learning Experience Questionnaire. Your successful completion of this questionnaire will aid us in gaining a deeper understanding of your important goals and objectives for your learning experience. Your completed questionnaire will be reviewed by a member of our Instructional Design team</p></div>
  </div>

  <div class="step" style="margin-top:45px">
    <h3 class="step-label">Mind Harbor Labs Conducts a High Level Assets Review<small>Phone meeting to discuss Steps 1 &amp; 2 and receive personalized guidance</small></h3>
    <div class="step-num">02</div>
    <div class="step-body">
      <p>Simultaneously, a member of our Instructional Design team will examine any content you have on hand that you would like to use to build your learning experience. Your Onboarding Specialist will provide you with a file-sharing link you can use to share your content with us. After concluding our High-Level Asset Review we will provide you with feedback regarding how your current content may work best in our platform.</p>
      <p>Once you have completed the Learning Experience Questionnaire and we have conducted our High-Level Asset Review, we will then meet with you by phone to discuss our findings and determine next steps.</p>
    </div>
  </div>
</section>

<section class="stage">
  <div class="stage-label">At this stage</div>
  <div class="stage-dot"></div>
  <p class="stage-text">Some clients are ready to work independently, while others may benefit from a more guided approach to the development of their learning experience. We'll let you decide whether you want to follow a <b>Self-Service</b> path or utilize our <b>Instructional Design Services</b>. Regardless of which path you take, we will provide you with access to the time-tested templates and processes used by our Instructional Design team.</p>
</section>

<section class="options">
  <div class="options-head"><strong>Based on the level of assistance you decide you need</strong>the next steps in this process generally unfold in the following order:</div>

  <div class="step">
    <div class="pair path-head">
      <div class="cell cell-self">Follow a<b>Self-Service</b></div>
      <div class="cell cell-guided">Utilizing MHL's<b>Instructional Design Service</b></div>
    </div>
  </div>

  <div class="step">
    <h3 class="step-label">Develop Your Learning Blueprint</h3>
    <div class="step-num">03</div>
    <div class="pair">
      <div class="cell cell-self">Develop your Learning Blueprint, which is like the Table of Contents in a book. This will help you organize your learning objectives into an information hierarchy.</div>
      <div class="cell cell-guided">A member of our Instructional Design team will work closely with you to develop your Learning Blueprint.<span class="aside">**We will work together in a series of phone meeting(s) and via email to collaborate, brainstorm, and review</span></div>
    </div>
  </div>

  <div class="step">
    <h3 class="step-label">Establish a Replicable Cadence for Your Learning Experience</h3>
    <div class="step-num">04</div>
    <div class="pair">
      <div class="cell cell-self">Establish a Replicable Cadence for your learning experience. Decide how you will open and close each section, determine how you will use formative and summative assessments and interactive tools, and determine how frequently you will use media (video, audio) to enhance learning.</div>
      <div class="cell cell-guided">We can help you to establish a Replicable Cadence for your learning experience. During this process, we will recommend the best tools to support your learners' engagement, assessments, and interactions. Utilizing your Learning Blueprint, we will recommend a structure you can use that will make the most of the tools of our platform and allow your content to shine.<span class="aside">**We will work together in a series of phone meeting(s) and via email to collaborate, brainstorm, and review</span></div>
    </div>
  </div>

  <div class="step">
    <h3 class="step-label">Populate Your Asset Inventory &amp; Planning Document</h3>
    <div class="step-num">05</div>
    <div class="pair">
      <div class="cell cell-self">Complete our Asset Inventory &amp; Planning Document, which will serve as both a gap analysis and a communication tool. Completing this document will help you identify the assets you will need to create for your learning experience. This can be used as a communication tool for your build-out team.</div>
      <div class="cell cell-guided">We will help you to complete your Asset Inventory &amp; Planning Document. We will use this as a communication tool for your build-out.<span class="aside">**We will work together in a series of phone meeting(s) and via email to collaborate, brainstorm, and review</span></div>
    </div>
  </div>

  <div class="step">
    <h3 class="step-label">Create Content as Needed</h3>
    <div class="step-num">06</div>
    <div class="pair">
      <div class="cell cell-self">Create additional content as needed.</div>
      <div class="cell cell-guided">We will guide and support you as you create any additional content you will need for your learning.</div>
    </div>
  </div>

  <div class="step">
    <h3 class="step-label">Upload Your Content to the Platform</h3>
    <div class="step-num">07</div>
    <div class="pair">
      <div class="cell cell-self">Upload your content to the platform or simply create content directly in the platform.</div>
      <div class="cell cell-guided">We will either work closely to support your team as they upload content or we will upload your content to the platform for you.</div>
    </div>
  </div>

  <div class="step">
    <h3 class="step-label">Preview Your Content in the Platform &amp; Make Necessary Adjustments</h3>
    <div class="step-num">08</div>
    <div class="pair">
      <div class="cell cell-self">Review your learning experience in the platform. Sometimes, when you see your content on the screen, it becomes apparent that changes may be necessary. Be sure to build in some time during this stage to modify your approach if needed.</div>
      <div class="cell cell-guided">Your Instructional Designer will review your learning experience in the platform, make recommendations for enhancing the learning experience, and, in some cases, make changes directly in the platform for you.</div>
    </div>
  </div>

  <div class="step plain">
    <h3 class="step-label" style="padding-top:16px">Launch!</h3>
    <div class="step-num">09</div>
    <div class="step-body" style="padding-top:24px;padding-left:28px">It's time to launch your learning experience.</div>
  </div>

  <div class="step plain">
    <h3 class="step-label">Post-Launch Check-In<small>Phone meeting to review and provide feedback</small></h3>
    <div class="step-num">10</div>
    <div class="step-body" style="padding-left:28px"><p>Once the first round of learners has made their way through your learning experience, our Instructional Design team likes to touch base with you one more time to see how it's going. In this Post-Launch Check-In Meeting we can look at the data generated within the course and walk through the results of student surveys you provide us to determine how well your course is hitting the desired mark. We will provide you with a few next steps you may want to take to further elevate your learning experience.</p></div>
  </div>

  <p class="closing">And then we can chat about your next learning experience<br>and begin the process again!</p>
</section>

<section class="outro">
  <p>No matter how simple or complex your online learning initiative is, our professional services team of project managers, developers, and designers can help you quickly and successfully get to market in weeks, not months.</p>
</section>

<footer class="footer">
  <div class="brand"><span class="brand-square"></span>Mind Harbor Labs</div>
  <div class="footer-url">www.mindharborlabs.com</div>
</footer>

<div class="timeline" aria-hidden="true"></div>

</body>
</html>
```